Marl-ow Sky Harbour Custom Brokers Limited

The Company deals with:
shipping
logistic
imports
Export
customs clearance (customs broker services); and
customers can shop online and we take care of the shipment from the United States of America to Jamaica.
(we offer freight forwarding services from USA to Kingston Jamaica
Our tagline is : Creating Waves in the Logistic Industry.
Address: Shop 6 Brindley Commercial Complex, 207-209 Pellman Road Kingston 8, Jamaica West Indies Telephone: (876)555-0192
Example of what we required can be seem: www.swiftparcelhubexample.com

```html
<!DOCTYPE html>
<html lang="en">
<head>
<meta charset="utf-8">
<title>Marl-ow Sky Harbour Custom Brokers Limited</title>
<link href="https://fonts.googleapis.com/css2?family=Roboto:wght@400;500;700;900&display=swap" rel="stylesheet">
<style>
:root{
  --navy:#0d2240;
  --navy-deep:#0a1c36;
  --gold:#f0aa00;
  --gold-dark:#e29d00;
  --ink:#1c2b44;
  --text:#555b66;
  --white:#fff;
  --sea1:#1a63b8;
  --sea2:#2f86d6;
  --photo-blue:#5f93c9;
  --photo-blue-soft:#86afd9;
}
*{margin:0;padding:0;box-sizing:border-box}
html,body{width:1200px;height:3008px;overflow:hidden}
body{font-family:'Roboto',sans-serif;color:var(--ink);background:var(--white);position:relative}
.abs{position:absolute}
a{color:inherit;text-decoration:none}

.topbar{left:0;top:0;width:1200px;height:30px;background:var(--navy);color:var(--white);font-size:13px;font-weight:500}
.topbar .welcome{left:63px;top:7px}
.topbar .login{left:922px;top:6px}
.topbar .socials{left:1054px;top:6px;display:flex;gap:6px}
.sq{display:block;width:16px;height:16px;background:var(--white);border-radius:2px}

.header{left:0;top:30px;width:1200px;height:108px;background:var(--white)}
.brand{left:86px;top:28px;display:flex;align-items:center;gap:10px}
.brand .dot{width:40px;height:40px;border-radius:50%;background:var(--gold)}
.brand .name{font-size:30px;font-weight:900;color:var(--navy);letter-spacing:1px}
.brand .sub{font-size:10px;font-weight:500;color:var(--navy);letter-spacing:1px;line-height:1.2}
.nav{left:470px;top:34px;display:flex;gap:40px;font-size:15px;font-weight:500;color:var(--navy)}
.nav .active{color:var(--gold)}
.call{left:969px;top:17px;line-height:1.25}
.call .lbl{color:var(--gold);font-size:17px;font-weight:500}
.call .num{color:var(--navy);font-size:21px;font-weight:700}

.hero{left:0;top:138px;width:1200px;height:615px;background:linear-gradient(135deg,var(--sea1),var(--sea2) 60%,#3a93de)}
.hero .title{left:0;width:1200px;text-align:center}
.hero .t1{top:122px;font-size:50px;font-weight:900;color:var(--gold)}
.hero .t2{top:180px;font-size:96px;font-weight:900;color:var(--white)}
.btn{display:inline-block;background:var(--gold);color:var(--white);font-weight:700;border-radius:30px;text-align:center}
.hero .reg{left:512px;top:310px;width:176px;height:48px;line-height:44px;font-size:17px;border:2px solid var(--white)}
.dots{left:554px;top:466px;display:flex;gap:14px}
.dots span{width:22px;height:7px;background:var(--white);border:2px solid var(--navy)}

.about-frame{left:621px;top:733px;width:491px;height:394px;border:6px solid var(--gold);background:linear-gradient(180deg,var(--photo-blue),var(--photo-blue-soft))}
.about-card{left:86px;top:750px;width:594px;height:361px;background:var(--white);box-shadow:0 0 8px rgba(0,0,0,.2);padding:38px 28px}
.about-card h2{font-size:40px;font-weight:900;color:var(--gold);margin-bottom:20px}
.about-card p{font-size:13.3px;line-height:21px;color:var(--text)}
.about-card .btn{margin-top:30px;width:154px;height:44px;line-height:44px;font-size:15px}

.sec-title{left:0;width:1200px;text-align:center;font-weight:900;color:var(--gold);font-size:40px}
.svc{top:1278px;width:247px;height:239px}
.svc.a{left:86px;background:linear-gradient(135deg,#c9a070,#8f8f8f)}
.svc.b{left:347px;background:linear-gradient(180deg,#5d7e9e,#3c4c5e)}
.svc.c{left:607px;background:linear-gradient(135deg,#c08a50,#e07a30 60%,#c69a66)}
.svc.d{left:866px;background:linear-gradient(90deg,#fbf7f1,#e8c4a6)}
.svc.b .inner{position:absolute;left:12px;top:20px;right:12px;bottom:20px;border:3px solid var(--gold);display:flex;align-items:center;justify-content:center;color:var(--white);font-weight:700;font-size:17px;background:rgba(20,40,70,.35)}
.arrow{width:24px;height:24px;background:var(--gold);top:1386px;display:flex;align-items:center;justify-content:center}

.calc{left:0;top:1608px;width:1200px;height:460px;background:linear-gradient(90deg,#21426d,#3c5f8c 55%,#a9bcd1)}
.calc .c{left:0;width:710px;text-align:center;color:var(--white)}
.calc h3{top:105px;font-size:39px;font-weight:700}
.calc .fee{top:178px;font-size:25px;font-weight:700;color:var(--gold)}
.calc .basis{top:206px;font-size:17px;font-weight:500}
.calc .note{top:240px;font-size:15.5px;font-weight:500;line-height:20px}
.calc .pw{left:224px;top:303px;width:262px;height:46px;background:var(--white);border:3px solid var(--gold);border-radius:30px;text-align:center;line-height:40px;font-size:14px;color:var(--text)}

.feat{top:2153px;width:174px;text-align:center}
.feat .ring{width:174px;height:174px;border:4px solid var(--gold);border-radius:50%;display:flex;align-items:center;justify-content:center}
.feat .lbl{margin-top:20px;font-size:19px;font-weight:500;color:var(--navy)}

.store{top:2542px;width:200px;text-align:center;font-size:36px;font-weight:700;color:var(--navy)}
.visit{left:638px;top:2589px;width:176px;height:44px;line-height:44px;font-size:18px}

.footer{left:0;top:2722px;width:1200px;height:286px;background:var(--navy);color:var(--white)}
.footer .fbrand{left:86px;top:40px;width:282px;text-align:center}
.fbrand .name{font-size:38px;font-weight:900;letter-spacing:2px}
.fbrand .sub{font-size:11px;letter-spacing:1.5px;margin-top:4px}
.fbrand p{font-size:13px;font-weight:500;line-height:21px;margin-top:30px}
.footer h4{font-size:17px;font-weight:700;color:var(--gold)}
.links{left:397px;top:24px}
.links li{list-style:none;font-size:13.5px;font-weight:500;margin-top:16px}
.contact{left:552px;top:24px;width:300px}
.contact .row{display:flex;gap:14px;font-size:13.5px;font-weight:500;line-height:21px;margin-top:14px}
.contact svg{flex:0 0 24px}
.news{left:870px;top:24px}
.news .field{margin-top:12px;display:flex;width:242px;height:44px}
.news .field span{flex:1;background:var(--white);color:#666;font-size:13px;padding:14px 10px}
.news .field b{width:44px;background:var(--gold);display:flex;align-items:center;justify-content:center}
.news .soc{display:flex;gap:12px;margin-top:20px}
.news .soc span{width:26px;height:26px;background:var(--gold);border-radius:3px}
.footer .rule{left:86px;top:238px;width:1026px;height:1px;background:#34496a}
.footer .copy{left:0;top:254px;width:1200px;text-align:center;font-size:15px;font-weight:500}
</style>
</head>
<body>

<div class="abs topbar">
  <span class="abs welcome">Welcome To Our Website</span>
  <span class="abs login">Login / Register</span>
  <span class="abs socials"><i class="sq"></i><i class="sq"></i><i class="sq"></i><i class="sq"></i></span>
</div>

<header class="abs header">
  <div class="abs brand">
    <span class="dot"></span>
    <div><div class="name">MSHS</div><div class="sub">MARL-OW SKY HARBOUR</div></div>
  </div>
  <nav class="abs nav"><a class="active">Home</a><a>About Us</a><a>Services</a><a>Blog</a><a>Contact Us</a></nav>
  <div class="abs call"><div class="lbl">Call Us Now</div><div class="num">(876)555-0192</div></div>
</header>

<section class="abs hero" role="img" aria-label="Aerial view of a container ship sailing on blue sea">
  <div class="abs title t1">WELCOME FOR</div>
  <div class="abs title t2">MSHS</div>
  <a class="abs btn reg">Register Now</a>
  <div class="abs dots"><span></span><span></span><span></span></div>
</section>

<div class="abs about-frame" role="img" aria-label="Plane, train and cargo ship photo"></div>
<section class="abs about-card">
  <h2>About Us</h2>
  <p>It is a long established fact that a reader will be distracted by the readable content of a page when looking at its layout. The point of using Lorem Ipsum is that it has a more -or-less normal distribution of letters, as opposed to using 'Content here, content here', making it look like readable English. It is a long established fact that a reader will be distracted by the readable content of a page when looking at its layout. The point of using Lorem Ipsum is that it has a more-or-less normal distribution of letters, as opposed to using 'Content here, content</p>
  <a class="btn">Read More &raquo;</a>
</section>

<h2 class="abs sec-title" style="top:1205px">Our Services</h2>
<div class="abs svc a" role="img" aria-label="Workers sorting boxes on a conveyor"></div>
<div class="abs svc b" role="img" aria-label="Port with cranes and trucks"><div class="inner">IMPORTS AND EXPORTS</div></div>
<div class="abs svc c" role="img" aria-label="Warehouse worker checking parcels"></div>
<div class="abs svc d" role="img" aria-label="Shopper paying online with a card"></div>
<div class="abs arrow" style="left:88px"><svg width="10" height="14" viewBox="0 0 10 14"><path d="M8 1 2 7l6 6" stroke="#fff" stroke-width="2.5" fill="none"/></svg></div>
<div class="abs arrow" style="left:1087px"><svg width="10" height="14" viewBox="0 0 10 14"><path d="M2 1l6 6-6 6" stroke="#fff" stroke-width="2.5" fill="none"/></svg></div>

<section class="abs calc" role="img" aria-label="Courier running with a hand truck of boxes over a city skyline">
  <h3 class="abs c">Shipping Weight Calculator</h3>
  <div class="abs c fee">Estimated freight cost/courier fee is: $: 0 USD.</div>
  <div class="abs c basis">(Based on weight of package only)</div>
  <div class="abs c note">Packages over $ 50.00 usd in value are subjected to Custom charges.<br>Please contact one of our offices for further details.</div>
  <div class="abs pw">Packages Weight</div>
</section>

<div class="abs feat" style="left:155px"><div class="ring"><svg width="104" height="80" viewBox="0 0 104 80"><g stroke="#0d2240" stroke-width="7" stroke-linecap="round" fill="none"><path d="M4 14h44M18 30h30M30 46h18"/><circle cx="68" cy="40" r="32"/><path d="M68 22v18l12 10"/></g></svg></div><div class="lbl">FAST</div></div>
<div class="abs feat" style="left:393px"><div class="ring"><svg width="80" height="90" viewBox="0 0 80 90"><path d="M22 38V24a18 18 0 0 1 36 0v14" stroke="#0d2240" stroke-width="9" fill="none"/><rect x="12" y="38" width="58" height="46" rx="6" fill="#0d2240"/><circle cx="41" cy="56" r="6" fill="#fff"/><rect x="38" y="58" width="6" height="14" fill="#fff"/></svg></div><div class="lbl">SECURE</div></div>
<div class="abs feat" style="left:632px"><div class="ring"><svg width="104" height="80" viewBox="0 0 104 80"><g fill="none" stroke="#0d2240" stroke-width="7"><path d="M10 28l78-18 8 36-78 18z"/><path d="M6 46c6 14 8 20 12 26l80-18"/></g><circle cx="52" cy="37" r="10" fill="#0d2240"/></svg></div><div class="lbl">AFFORDABLE</div></div>
<div class="abs feat" style="left:870px"><div class="ring"><svg width="110" height="80" viewBox="0 0 110 80"><g fill="none" stroke="#0d2240" stroke-width="7"><rect x="46" y="6" width="58" height="44"/><path d="M46 24H26L8 42v16h96"/><circle cx="26" cy="62" r="9" fill="#fff"/><circle cx="86" cy="62" r="9" fill="#fff"/><path d="M58 42l30-30M72 44l24-24"/></g></svg></div><div class="lbl">COVENIENT</div></div>

<h2 class="abs sec-title" style="top:2440px">Online Stores</h2>
<div class="abs store" style="left:110px">Parcelia</div>
<div class="abs store" style="left:350px">VoltMart</div>
<div class="abs store" style="left:625px;top:2510px">Bidora</div>
<div class="abs store" style="left:892px">Grovemart</div>
<a class="abs btn visit">Visit Website</a>

<footer class="abs footer">
  <div class="abs fbrand">
    <div class="name">MSHS</div>
    <div class="sub">MARL-OW SKY HARBOUR</div>
    <p>It is a long established fact that a reader will be distracted by the readable content of a page when looking at its layout.</p>
  </div>
  <div class="abs links"><h4>QUICK LINKS</h4><ul><li>Home</li><li>About Us</li><li>Services</li><li>Blog</li><li>Contact Us</li></ul></div>
  <div class="abs contact"><h4>CONTACT US</h4>
    <div class="row"><svg width="24" height="24" viewBox="0 0 24 24"><path d="M12 2a7 7 0 0 0-7 7c0 5 7 13 7 13s7-8 7-13a7 7 0 0 0-7-7z" fill="#f0aa00"/><circle cx="12" cy="9" r="3" fill="#0d2240"/></svg><span>Shop 6 Brindley Commercial Complex, 207-209 Pellman Road Kingston 8, Jamaica West Indies</span></div>
    <div class="row"><svg width="24" height="24" viewBox="0 0 24 24"><path d="M6 2l4 5-2 3c1 3 3 5 6 6l3-2 5 4-3 4C10 22 2 14 2 5z" fill="#f0aa00"/></svg><span>(876)555-0192</span></div>
    <div class="row"><svg width="24" height="24" viewBox="0 0 24 24"><rect x="1" y="5" width="22" height="15" fill="#f0aa00"/><path d="M1 5l11 8 11-8" stroke="#0d2240" stroke-width="2" fill="none"/></svg><span>info@marlowskyharbour.example</span></div>
  </div>
  <div class="abs news"><h4>NEWSLETTER</h4>
    <div class="field"><span>Enter Email</span><b><svg width="22" height="22" viewBox="0 0 22 22"><circle cx="9" cy="9" r="6.5" stroke="#fff" stroke-width="3" fill="none"/><path d="M14 14l6 6" stroke="#fff" stroke-width="3"/></svg></b></div>
    <div class="soc"><span></span><span></span><span></span><span></span></div>
  </div>
  <div class="abs rule"></div>
  <div class="abs copy">Copyrights © Company Name 2020. All rights reserved.</div>
</footer>

</body>
</html>
```